Company Stationary

I'd like a template to use for company stationery. We frequently write short 1 - 2 page Word documents (which we save as PDF) to clients and prospects and the presentation is boring and doesn't look professional. I am looking for a Word template that will convey a better sense of professionalism. The design should include our logo (attached) but be simple and elegant. It should save nicely as a PDF, since that is how we will send the files via email.

Target Market(s)

Financial Institutions

Industry/Entity Type

Financial Service

Font styles to use
Serif

Colors

Designer to choose colors to be used in the design.

Requirements
Must have
• Simple design. Needs to be subtle. I don't want the design to be more interesting than the message we are writing.
Nice to have
• When the reader sees it, I want them to feel they are reading something published by a large, very successful company.
Should not have
• Not overpowering design and colors.

```html
<!DOCTYPE html>
<html lang="en">
<head>
<meta charset="utf-8">
<title>Clarivest Letterhead</title>
<link rel="stylesheet" href="https://fonts.googleapis.com/css2?family=Source+Serif+4:opsz,wght@8..60,400;8..60,600;8..60,700&display=swap">
<style>
  :root {
    --backdrop: #e9e9ea;
    --paper: #ffffff;
    --ink: #1c1c1c;
    --accent-red: #8f1d1d;
    --accent-dark: #2a2a2a;
    --rule: #8a8a8a;
    --band-text: #f4e9e9;
    --signature-tone: #e2e2e2;
  }
  * { margin: 0; padding: 0; box-sizing: border-box; }
  html, body {
    width: 1200px; height: 815px; overflow: hidden;
    background: var(--backdrop);
    font-family: "Source Serif 4", Georgia, serif;
    color: var(--ink);
  }
  .canvas { position: relative; width: 1200px; height: 815px; }
  .sheet {
    position: absolute; background: var(--paper);
    box-shadow: 0 6px 22px rgba(0,0,0,0.16);
  }
  .sheet--letter { left: 80px; top: 64px; width: 490px; height: 693px; }
  .sheet--blank  { left: 636px; top: 70px; width: 488px; height: 689px; }
  .side-band { position: absolute; right: 0; top: 0; width: 14px; height: 100%; }
  .side-band svg { display: block; width: 14px; height: 100%; }
  .band-url {
    position: absolute; right: 0; top: 32px; width: 14px;
    writing-mode: vertical-rl;
    color: var(--band-text); font-size: 9.5px; letter-spacing: 1.6px;
    line-height: 14px; text-align: left;
  }
  .brand {
    position: absolute; left: 32px; top: 34px;
    display: flex; align-items: center; gap: 6px;
    font-weight: 700; font-size: 26px; line-height: 30px;
    color: var(--ink); letter-spacing: 0.2px;
  }
  .brand-mark { width: 8px; height: 8px; background: var(--accent-red); }
  .contact {
    position: absolute; left: 364px; top: 34px;
    border-left: 1px solid var(--rule); padding-left: 10px;
    font-style: normal; font-size: 7.4px; line-height: 8.9px; height: 54px;
  }
  .contact-row { display: flex; align-items: center; gap: 5px; }
  .contact-icon { width: 7px; height: 7px; fill: var(--accent-red); flex: none; }
  .contact-gap { height: 3px; }
  .letter-body {
    position: absolute; left: 32px; top: 204px; width: 356px;
    font-size: 7.6px; line-height: 11.6px;
  }
  .letter-body p { margin-bottom: 11.6px; }
  .signature {
    position: absolute; left: 37px; top: 480px; width: 140px; height: 22px;
    background: var(--signature-tone); border-radius: 2px;
  }
</style>
</head>
<body>
<main class="canvas">

  <section class="sheet sheet--letter">
    <div class="brand"><span>Clarivest</span><span class="brand-mark"></span></div>

    <address class="contact">
      <div>Clarivest, LLC</div>
      <div>218 Orchard Lane</div>
      <div>Fairhaven, NJ 07190</div>
      <div class="contact-gap"></div>
      <div class="contact-row">
        <svg class="contact-icon" viewBox="0 0 10 10"><path d="M2 0.5 L3.8 2.6 L2.9 3.8 Q4 6 6.2 7.1 L7.4 6.2 L9.5 8 L8.2 9.5 Q1 8 0.5 1.8 Z"/></svg>
        <span>(555) 014-2270</span>
      </div>
      <div class="contact-row">
        <svg class="contact-icon" viewBox="0 0 10 10"><rect x="2.5" y="0.5" width="5" height="3"/><rect x="0.5" y="3.8" width="9" height="4"/><rect x="2.5" y="7" width="5" height="2.5"/></svg>
        <span>(555) 014-2281</span>
      </div>
      <div class="contact-row">
        <svg class="contact-icon" viewBox="0 0 10 10"><path d="M0.5 2 H9.5 V8 H0.5 Z M0.5 2 L5 5.5 L9.5 2" stroke="#fff" stroke-width="0.8"/></svg>
        <span>hello@clarivest.example</span>
      </div>
    </address>

    <div class="letter-body">
      <p>Lorem ipsum dolor sit amet, consectetur adipiscing elit. Praesent non est diam. Vivamus risus sem, gravida sit amet nibh ut, ornare lobortis ante. Aliquam sollicitudin, mauris tincidunt semper venenatis, orci est pretium augue, ut vestibulum felis velit bibendum urna. Integer sollicitudin aliquet ligula, non ultricies nisl efficitur nec. Aliquam felis lorem, facilisis ac condimentum quis, consectetur volutpat lacus. Proin fermentum sem quis elit efficitur, eu tempus magna maximus.</p>
      <p>&nbsp;Aenean a mi tortor. Morbi pretium mi sed cursus vehicula. Lorem ipsum dolor sit amet, consectetur adipiscing elit. In finibus eros ac maximus finibus. Nunc pretium pellentesque tellus. Nullam accumsan nisl non diam commodo sagittis. Nunc et ante sit amet urna auctor convallis. Maecenas sed fringilla metus, sit amet vulputate felis. Morbi eget tempor nisi. Aliquam erat volutpat. Aenean laoreet interdum tempus.</p>
      <p>&nbsp;Maecenas dignissim placerat mauris, vitae sollicitudin ex. Integer bibendum maximus mauris, ac tempor urna viverra id. Integer tincidunt lobortis nisl at posuere. Sed faucibus vulputate finibus. Maecenas convallis, sem quis pellentesque cursus, urna quam aliquam augue, quis porttitor eros est nec lectus. Sed mattis at tellus ut blandit. Aenean nunc magna, viverra sed mauris vel, porta finibus lacus. Nullam bibendum turpis rutrum porta placerat</p>
      <p>Aenean a mi tortor. Morbi pretium mi sed cursus vehicula. Lorem ipsum dolor sit amet, consectetur adipiscing elit. In finibus eros ac maximus finibus. Nunc pretium pellentesque tellus. Nullam accumsan nisl non diam commodo sagittis. Nunc et ante sit amet urna auctor convallis. Maecenas sed fringilla metus, sit amet vulputate felis. Morbi eget tempor nisi. Aliquam erat volutpat. Aenean laoreet interdum tempus. .</p>
    </div>

    <div class="signature" role="img" aria-label="Handwritten signature of Daniel Reyes"></div>

    <div class="side-band">
      <svg viewBox="0 0 14 693" preserveAspectRatio="none">
        <polygon points="0,0 14,0 14,550 0,538" fill="var(--accent-red)"/>
        <polygon points="0,545 14,557 14,693 0,693" fill="var(--accent-dark)"/>
      </svg>
      <div class="band-url">www.clarivest.example</div>
    </div>
  </section>

  <section class="sheet sheet--blank">
    <div class="brand"><span>Clarivest</span><span class="brand-mark"></span></div>
    <div class="side-band">
      <svg viewBox="0 0 14 689" preserveAspectRatio="none">
        <polygon points="0,0 14,0 14,552 0,540" fill="var(--accent-red)"/>
        <polygon points="0,547 14,559 14,689 0,689" fill="var(--accent-dark)"/>
      </svg>
      <div class="band-url">www.clarivest.example</div>
    </div>
  </section>

</main>
</body>
</html>
```